Brochure Lantern Ridge Advisory

need brochure to display my services. We are a business consulting firm focused on small to medium size business. We also do speaking engagements and trainings on leadership development as well as help local suppliers bring products to mark
et. I have some specific ideas regarding setup. Would like to follow color scheme of my logo and my business cards. Like the black background. Also with setup would like the following:
Cover - Logo and Mission statement
Back - Bio
Inside( fully opened brochure) array of services separated by catagory
inside flap - mission/vision/purpose
I will upload sketch of this as well as Mission/Vision/Purpose statements

Target Market(s)

small to medium size business owners
local vendors
any purveyor of services or goods

Industry/Entity Type

Business Consultant

Font styles to use
Serif

Requirements
Must have
• want to include the following:
• Logo
• contact information
• bio
• array of services
• mission/vision/purpose statement - to be added to files later today
Nice to have
• Cover: Logo, Mission statement
• Back : Bio
• Inside: array of services on 3 inside pages; broken out onto 3 categories, 1 per page.
• will upload sketch of this

```html
<!DOCTYPE html>
<html lang="en">
<head>
<meta charset="utf-8">
<title>Lantern Ridge Advisory – Trifold Brochure</title>
<link href="https://fonts.googleapis.com/css2?family=Oswald:wght@500;600&family=Open+Sans:wght@400;600&display=swap" rel="stylesheet">
<style>
  :root{
    --ink:#121212;
    --ink-soft:#1d1d1d;
    --orange:#f07c1e;
    --green:#7ab51d;
    --white:#ffffff;
    --text:#e6e6e6;
    --paper:#ffffff;
    --photo-warm:linear-gradient(150deg,#d9b48a,#a8713f 55%,#6b4223);
    --photo-bright:linear-gradient(150deg,#e9dccb,#c29a6c 50%,#8a5a31);
    --photo-cool:linear-gradient(150deg,#d8dde0,#9aa3a8 55%,#5c6468);
  }
  *{box-sizing:border-box;margin:0;padding:0}
  html,body{width:887px;height:1200px;overflow:hidden;background:var(--paper)}
  body{position:relative;font-family:"Open Sans",Arial,sans-serif;color:var(--text)}
  .sheet{position:absolute;left:0;width:887px;height:594px;background:var(--ink);overflow:hidden}
  .sheet--outside{top:0}
  .sheet--inside{top:606px}
  .panel{position:absolute;top:0;width:296px;height:594px}
  .panel--1{left:0}.panel--2{left:296px}.panel--3{left:592px}
  .photo{position:absolute;background:var(--photo-warm)}
  .swoosh{position:absolute;left:0;width:100%}
  .heading{font-family:"Oswald",Arial,sans-serif;font-weight:600;text-transform:uppercase;color:var(--orange);letter-spacing:.5px}
  .body-copy{font-size:7.4px;line-height:1.5;color:var(--text)}
  .body-copy p+p{margin-top:7px}

  /* outside – left flap */
  .flap-photo{left:0;top:0;width:296px;height:225px;background:var(--photo-bright)}
  .statements{position:absolute;left:18px;top:232px;width:200px}
  .statements .heading{font-size:12px;margin:10px 0 3px}
  .contact{position:absolute;left:18px;bottom:14px;font-size:8px;color:var(--white);display:flex;gap:14px;align-items:center}
  .contact svg{width:9px;height:9px;vertical-align:-1px;margin-right:3px}

  /* outside – bio panel */
  .portrait{left:108px;top:12px;width:80px;height:80px;border-radius:50%;border:3px solid var(--orange);background:var(--photo-warm)}
  .bio-name{position:absolute;top:100px;width:100%;text-align:center;font-size:13px}
  .bio{position:absolute;left:20px;right:20px;top:124px;text-align:justify}

  /* outside – cover */
  .cover-photo{left:0;top:0;width:296px;height:320px;background:var(--photo-bright)}
  .brand{position:absolute;top:345px;width:100%;text-align:center}
  .brand-dot{display:block;margin:0 auto 8px;width:14px;height:14px;border-radius:50%;background:var(--green)}
  .brand-name{font-family:"Oswald",Arial,sans-serif;font-weight:500;font-size:19px;letter-spacing:1.5px;text-transform:uppercase;color:var(--green);line-height:1.15}
  .tagline{position:absolute;left:0;right:0;top:440px;padding:10px 18px 12px;background:var(--orange);color:var(--white)}
  .tagline strong{display:block;font-family:"Oswald",Arial,sans-serif;font-weight:600;font-size:18px;letter-spacing:.5px}
  .tagline span{font-family:"Oswald",Arial,sans-serif;font-size:9.5px;letter-spacing:1px;text-transform:uppercase}
  .website{position:absolute;bottom:16px;width:100%;text-align:center;font-family:"Oswald",Arial,sans-serif;font-size:11px;letter-spacing:1.5px;color:var(--white)}

  /* inside */
  .team-photo{left:0;top:0;width:592px;height:330px}
  .speaker-photo{left:592px;top:0;width:295px;height:330px;background:var(--photo-cool)}
  .service-block{position:absolute}
  .service-block .heading{font-size:12px;margin-bottom:6px}
  .service-list{list-style:none;font-size:8px;line-height:1.55;color:var(--white)}
  .service-list li::before{content:"";display:inline-block;width:4px;height:4px;background:var(--green);margin-right:6px;vertical-align:1px}
  .cols{display:flex;gap:18px}
  .products{left:18px;top:438px}
  .office-photo{left:332px;top:390px;width:92px;height:62px;border:2px solid var(--white);background:var(--photo-bright)}
  .support{left:314px;top:468px}
  .lectures{left:610px;top:400px;width:260px}
  .lectures .body-copy{margin-top:12px;text-align:justify}
</style>
</head>
<body>

<section class="sheet sheet--outside" aria-label="Brochure outside">
  <div class="panel panel--1">
    <div class="photo flap-photo" role="img" aria-label="Photo of a baker holding a tray of fresh pastries"></div>
    <svg class="swoosh" style="top:180px" width="296" height="60" viewBox="0 0 296 60" aria-hidden="true">
      <path d="M0 30 C90 50 200 20 296 0 L296 60 L0 60Z" fill="var(--ink)"/>
      <path d="M0 26 C90 46 200 16 296 -4 L296 4 C200 24 90 54 0 34Z" fill="var(--orange)"/>
      <path d="M0 36 C90 56 200 26 296 6 L296 11 C200 31 90 61 0 41Z" fill="var(--green)"/>
    </svg>
    <div class="statements body-copy">
      <h3 class="heading">Mission</h3>
      <p>To encourage and support the growth of small to medium size businesses through practical guidance.</p>
      <h3 class="heading">Vision</h3>
      <p>A thriving local economy where every owner, vendor and maker has the tools to lead with confidence and purpose.</p>
      <h3 class="heading">Purpose</h3>
      <p>We listen first, plan with care and stay beside our clients until each goal is reached.</p>
    </div>
    <div class="contact">
      <span><svg viewBox="0 0 10 10"><path d="M2 1h2l1 2.5-1.2.8a5 5 0 0 0 2 2l.8-1.2L9 6v2l-1 1C4 9 1 6 1 2z" fill="var(--orange)"/></svg>(555) 014-2288</span>
      <span>hello@lanternridgeadvisory.com</span>
    </div>
  </div>

  <div class="panel panel--2">
    <div class="photo portrait" role="img" aria-label="Portrait of the firm's founder"></div>
    <h2 class="heading bio-name">Marla Whitcombe</h2>
    <div class="bio body-copy">
      <p>Marla Whitcombe founded Lantern Ridge Advisory after two decades helping owners turn small shops into steady, growing companies. She began her career in retail operations, later leading regional teams in finance, purchasing and staff training, where she learned that lasting growth starts with clear goals and honest numbers.</p>
      <p>Today Marla works side by side with owners of small and medium size businesses, local vendors and independent makers. She helps them sharpen their plans, build stronger teams and bring new products from the kitchen table to the store shelf. Her approach is simple: listen closely, measure what matters and act with care.</p>
      <p>As a speaker and trainer, Marla leads workshops on leadership development, customer service and team culture. Her sessions are known for warmth, humour and practical tools that participants can put to use the very next morning.</p>
      <p>Marla serves on the board of a local small business network and mentors new owners through community programs. She believes that strong local businesses build strong neighbourhoods, and that every owner deserves a partner who cares about their success as much as they do.</p>
      <p>When she is not working with clients, Marla enjoys gardening, long walks with her family and visiting the farmers market every Saturday morning.</p>
    </div>
  </div>

  <div class="panel panel--3">
    <div class="photo cover-photo" role="img" aria-label="Photo of smiling bakery staff behind a counter of fresh bread"></div>
    <svg class="swoosh" style="top:280px" width="296" height="60" viewBox="0 0 296 60" aria-hidden="true">
      <path d="M0 0 C100 30 200 44 296 34 L296 60 L0 60Z" fill="var(--ink)"/>
      <path d="M0 -4 C100 26 200 40 296 30 L296 36 C200 46 100 32 0 2Z" fill="var(--green)"/>
      <path d="M0 4 C100 34 200 48 296 38 L296 42 C200 52 100 38 0 8Z" fill="var(--orange)"/>
    </svg>
    <div class="brand">
      <span class="brand-dot"></span>
      <div class="brand-name">Lantern Ridge<br>Advisory</div>
    </div>
    <div class="tagline">
      <strong>TO ENCOURAGE AND SUPPORT</strong>
      <span>The growth of small to medium size business</span>
    </div>
    <div class="website">www.lanternridgeadvisory.com</div>
  </div>
</section>

<section class="sheet sheet--inside" aria-label="Brochure inside">
  <div class="photo team-photo" role="img" aria-label="Photo of three smiling bakery workers with trays of bread"></div>
  <div class="photo speaker-photo" role="img" aria-label="Photo of a consultant in glasses smiling"></div>
  <svg class="swoosh" style="top:270px" width="887" height="110" viewBox="0 0 887 110" preserveAspectRatio="none" aria-hidden="true">
    <path d="M0 40 C200 90 420 70 592 30 C700 5 800 20 887 60 L887 110 L0 110Z" fill="var(--ink)"/>
    <path d="M0 32 C200 82 420 62 592 22 C700 -3 800 12 887 52 L887 60 C800 20 700 5 592 30 C420 70 200 90 0 40Z" fill="var(--orange)"/>
    <path d="M0 44 C200 94 420 74 592 34 C700 9 800 24 887 64 L887 69 C800 29 700 14 592 39 C420 79 200 99 0 49Z" fill="var(--green)"/>
  </svg>

  <div class="service-block products">
    <h3 class="heading">Products to Market</h3>
    <div class="cols">
      <ul class="service-list">
        <li>Product Development</li>
        <li>Business Plans</li>
        <li>Marketing</li>
        <li>Logistics</li>
      </ul>
      <ul class="service-list">
        <li>Positioning</li>
        <li>Distribution</li>
        <li>Research &amp; Development</li>
      </ul>
    </div>
  </div>

  <div class="photo office-photo" role="img" aria-label="Photo of a small storefront building"></div>
  <div class="service-block support">
    <h3 class="heading">Business Support</h3>
    <div class="cols">
      <ul class="service-list">
        <li>Start Ups</li>
        <li>Business Plans</li>
        <li>Marketing Strategies</li>
        <li>Merchandising</li>
        <li>Sales Growth</li>
      </ul>
      <ul class="service-list">
        <li>Profitability</li>
        <li>Training &amp; Development</li>
        <li>Recruiting &amp; Hiring</li>
        <li>Operations</li>
        <li>Research &amp; Development</li>
      </ul>
    </div>
  </div>

  <div class="service-block lectures">
    <h3 class="heading">Lectures &amp; Seminars</h3>
    <div class="cols">
      <ul class="service-list">
        <li>Training</li>
        <li>Leadership</li>
      </ul>
      <ul class="service-list">
        <li>Motivational</li>
        <li>Team Building</li>
      </ul>
    </div>
    <div class="body-copy">
      <p>Our engaging talks and workshops give owners, managers and teams fresh energy and practical tools. Each session is shaped around your goals, from leading through change to building a culture where people want to stay and grow.</p>
      <p>We speak at conferences, chamber events and company retreats, and offer hands-on training programs that continue long after the event ends, with follow-up coaching to keep progress on track.</p>
    </div>
  </div>
</section>

</body>
</html>
```